K P Guard Services - Alarm and CCTV installation Flyer

Need a flyer designed that grabs the attention of potential customers, we need the price to stand out the most to grab people’s attention, whether they are residential or commercial.We are a security company based in Brentwood Essex but cover London and the home counties. here is our website to take a look at www.kpguardservices.co.uk. We want them to know we install complete alarm and Cctv systems and will keep them “safe”

Target Market(s)

residential and commercial property

Colors
f37122

Requirements
Must have
• on one side
• large clear logo - professional design
• - Intruder Alarms starting from £495 + VAT. (Big text)
• - £150 discount on installations
• *terms and conditions apply (small text)
• - Not happy with your current provider? Free of charge no obligation take over survey and quotation and up to £100 off
• - CCTV systems starting from £595 + VAT (based on 2 cameras)
• K P Guard Services are always there, always available, wherever and whenever you need us.
• Large telephone number at the bottom 01632 480913
• Address / email / website as a footer * see website for details
• on second side
• large and bold
• Are you looking to keep you and your premises safe?
• - K P Guard Services install, maintain and repair all intruder alarms, CCTV, intercom and access control
• - View, control and manage your security systems anywhere in the world
• - Feel at ease with monitoring services & police response tailored to suit you and your business
• - K P Guard can takeover any existing security system and offer maintenance checks to guarantee the best performance for you and your premises
• - K P Guard understand that being security conscious is ever increasing, protecting your property and family is a number one priority
• - Our fully insured and accredited team offer quality, safety and cost efficiency throughout the whole process
• - K P Guard Services are using the latest cloud-based technology to stay connected with your home and business 24/7
• If you are looking to improve the security in your home, office or commercial property then call a member of our team today for a free quote.
• Fully insured and accredited
• Jobrater logo and NQRB Intruder and CCTV logos
• Logo somewhere on page and
• Telephone number
• Address / email / website as footer
Nice to have
• We would like to have the text saying
• Intruder alarms installed from £495 + vat the biggest text on the page. Most likely the £495 part the largest.
• Also would like “not happy with your current provider” more obvious
• We would like use our company colours - Orange/White/black

```html
<!DOCTYPE html>
<html lang="en">
<head>
<meta charset="utf-8">
<title>K P Guard Services – Alarm and CCTV Flyer</title>
<link rel="stylesheet" href="https://fonts.googleapis.com/css2?family=Exo+2:ital,wght@0,300;0,400;0,600;0,700;0,800;1,700&display=swap">
<style>
  :root {
    --orange: #f37122;
    --black: #000000;
    --white: #ffffff;
    --ink: #111111;
  }
  * { box-sizing: border-box; margin: 0; padding: 0; }
  html, body { width: 846px; height: 1200px; overflow: hidden; background: var(--white); }
  body { font-family: "Exo 2", Arial, sans-serif; }

  .flyer { position: relative; width: 846px; height: 1200px; background: var(--white); overflow: hidden; }

  /* Brand header */
  .brand-mark { position: absolute; left: 62px; top: 28px; width: 160px; height: 160px; background: var(--orange); }
  .brand-name { position: absolute; left: 258px; top: 36px; width: 540px; color: var(--ink); text-align: center; line-height: 1; }
  .brand-name .line-1 { display: block; font-weight: 800; font-size: 84px; letter-spacing: 1px; white-space: nowrap; }
  .brand-name .line-2 { display: flex; align-items: center; justify-content: space-between; margin-top: 22px; font-weight: 300; font-size: 50px; letter-spacing: 7px; }
  .brand-name .rule { display: block; width: 102px; height: 6px; background: var(--ink); }

  /* Panels */
  .panel { position: absolute; background: var(--black); }
  .dot { position: absolute; width: 40px; height: 40px; border-radius: 50%; background: var(--orange); }

  .panel-alarms { left: 75px; top: 250px; width: 712px; height: 177px; text-align: center; }
  .panel-alarms .heading { color: var(--orange); font-weight: 700; font-size: 41px; margin-top: 14px; white-space: nowrap; }
  .price-tag { position: absolute; left: 116px; top: 73px; width: 494px; height: 87px; background: var(--orange); color: var(--white); display: flex; align-items: center; justify-content: center; gap: 10px; }
  .price-tag .amount { font-weight: 800; font-size: 76px; }
  .price-tag .vat { font-weight: 400; font-size: 56px; }

  .panel-switch { left: 75px; top: 455px; width: 339px; height: 394px; text-align: center; }
  .panel-switch .question { color: var(--white); font-weight: 700; font-style: italic; font-size: 30px; line-height: 1.3; margin-top: 26px; }
  .panel-switch .offer { color: var(--orange); font-weight: 400; font-size: 25px; line-height: 1.36; margin-top: 8px; }
  .saving-tag { position: absolute; left: 42px; top: 329px; width: 256px; height: 44px; background: var(--orange); color: var(--white); font-size: 20px; display: flex; align-items: center; justify-content: center; gap: 4px; }
  .saving-tag strong { font-size: 30px; font-weight: 800; }

  .panel-discount { left: 447px; top: 455px; width: 340px; height: 177px; text-align: center; }
  .discount-tag { position: absolute; left: 39px; top: 15px; width: 262px; height: 43px; background: var(--orange); color: var(--white); font-weight: 700; font-size: 30px; display: flex; align-items: center; justify-content: center; }
  .panel-discount .label { position: absolute; left: 0; right: 0; top: 70px; color: var(--orange); font-size: 23px; line-height: 1.4; }
  .panel-discount .terms { position: absolute; left: 0; right: 0; top: 144px; color: var(--white); font-size: 16px; }

  .panel-cctv { left: 447px; top: 664px; width: 340px; height: 188px; text-align: center; }
  .panel-cctv .label { color: var(--orange); font-size: 23px; line-height: 1.35; margin-top: 18px; }
  .cctv-tag { position: absolute; left: 45px; top: 87px; width: 264px; height: 45px; background: var(--orange); color: var(--white); font-size: 20px; display: flex; align-items: center; justify-content: center; gap: 6px; }
  .cctv-tag strong { font-size: 26px; font-weight: 800; }
  .panel-cctv .note { position: absolute; left: 0; right: 0; top: 146px; color: var(--white); font-size: 19px; }

  /* Tagline */
  .tagline { position: absolute; left: 0; right: 0; top: 866px; text-align: center; font-weight: 700; font-style: italic; font-size: 28px; line-height: 1.28; color: var(--ink); white-space: nowrap; }
  .tagline .company { color: var(--orange); }

  /* Phone band */
  .phone-band { position: absolute; left: 0; top: 944px; width: 846px; height: 134px; background: var(--black); overflow: hidden; }
  .phone-icon { position: absolute; left: 12px; top: 30px; width: 74px; height: 74px; }
  .phone-number { position: absolute; left: 100px; top: 0; height: 134px; display: flex; align-items: center; color: var(--white); font-weight: 800; font-size: 118px; letter-spacing: 1px; line-height: 1; white-space: nowrap; transform: scaleX(0.84); transform-origin: left center; }

  /* Footer */
  .contact-footer { position: absolute; left: 0; top: 1078px; width: 846px; height: 122px; background: var(--orange); color: var(--white); text-align: center; font-weight: 700; font-size: 22px; line-height: 1.45; padding-top: 12px; white-space: nowrap; }
  .contact-footer .label { font-weight: 600; }
</style>
</head>
<body>
<main class="flyer">

  <header>
    <div class="brand-mark" aria-hidden="true"></div>
    <h1 class="brand-name">
      <span class="line-1">K P GUARD</span>
      <span class="line-2"><span class="rule"></span>SERVICES<span class="rule"></span></span>
    </h1>
  </header>

  <span class="dot" style="left:57px; top:231px;"></span>
  <section class="panel panel-alarms">
    <h2 class="heading">Intruder Alarms starting from</h2>
    <div class="price-tag"><span class="amount">£495</span><span class="vat">+ VAT</span></div>
  </section>

  <span class="dot" style="left:57px; top:434px;"></span>
  <section class="panel panel-switch">
    <p class="question">Not happy<br>with your current<br>provider?</p>
    <p class="offer">Free of charge<br>no obligation<br>take over<br>survey and<br>quotation and</p>
    <div class="saving-tag">up to <strong>£100</strong> off</div>
  </section>

  <span class="dot" style="left:427px; top:434px;"></span>
  <section class="panel panel-discount">
    <div class="discount-tag">£150</div>
    <p class="label">discount<br>on installations</p>
    <p class="terms">*terms and conditions apply</p>
  </section>

  <span class="dot" style="left:427px; top:641px;"></span>
  <section class="panel panel-cctv">
    <p class="label">CCTV systems starting<br>from £595 + VAT</p>
    <div class="cctv-tag"><strong>£595</strong> + VAT</div>
    <p class="note">(based on 2 cameras)</p>
  </section>

  <p class="tagline"><span class="company">K P Guard Services</span> are always there, always<br>available, wherever and whenever you need us.</p>

  <section class="phone-band">
    <svg class="phone-icon" viewBox="0 0 74 74" aria-hidden="true" fill="none" stroke="#f37122" stroke-width="3" stroke-linecap="round">
      <rect x="23" y="8" width="28" height="58" rx="5"/>
      <line x1="23" y1="16" x2="51" y2="16"/>
      <line x1="23" y1="56" x2="51" y2="56"/>
      <circle cx="37" cy="61" r="1.5" fill="#f37122" stroke="none"/>
      <path d="M16 28 q-5 9 0 18"/>
      <path d="M9 24 q-8 13 0 26"/>
      <path d="M58 28 q5 9 0 18"/>
      <path d="M65 24 q8 13 0 26"/>
    </svg>
    <p class="phone-number">01632 480913</p>
  </section>

  <footer class="contact-footer">
    <p><span class="label">address:</span> 14 Warley Lane, Brentwood, Essex, CM14-7QX</p>
    <p><span class="label">email:</span> operations@kpguardservices.co.uk</p>
    <p><span class="label">website:</span> www.kpguardservices.co.uk</p>
  </footer>

</main>
</body>
</html>
```